Company Stationary

I'd like a template to use for company stationery. We frequently write short 1 - 2 page Word documents (which we save as PDF) to clients and prospects and the presentation is boring and doesn't look professional. I am looking for a Word template that will convey a better sense of professionalism. The design should include our logo (attached) but be simple and elegant. It should save nicely as a PDF, since that is how we will send the files via email.

Target Market(s)

Financial Institutions

Industry/Entity Type

Financial Service

Font styles to use
Serif

Colors

Designer to choose colors to be used in the design.

Requirements
Must have
• Simple design. Needs to be subtle. I don't want the design to be more interesting than the message we are writing.
Nice to have
• When the reader sees it, I want them to feel they are reading something published by a large, very successful company.
Should not have
• Not overpowering design and colors.

```html
<!DOCTYPE html>
<html lang="en">
<head>
<meta charset="utf-8">
<title>Meridale Stationery</title>
<link href="https://fonts.googleapis.com/css2?family=Archivo:wght@400;700&display=swap" rel="stylesheet">
<style>
  :root {
    --bg: #e3e3e3;
    --paper: #ffffff;
    --ink: #141414;
    --muted: #4a4a4a;
    --red: #c02424;
    --card: #1e1e1e;
    --card-mark: #2c2c2c;
    --card-text: #d8d8d8;
  }
  * { margin: 0; padding: 0; box-sizing: border-box; }
  html, body { width: 1200px; height: 960px; overflow: hidden; }
  body {
    background: var(--bg);
    font-family: "Archivo", Arial, sans-serif;
    color: var(--ink);
    position: relative;
  }
  .wordmark { font-weight: 700; letter-spacing: 0.5px; line-height: 1; }
  .icon { width: 10px; height: 10px; flex: none; }

  /* Letterhead */
  .letterhead {
    position: absolute; left: 50px; top: 120px;
    width: 450px; height: 636px;
    background: var(--paper);
    box-shadow: 0 2px 8px rgba(0,0,0,.12);
  }
  .letterhead .wordmark { position: absolute; left: 40px; top: 40px; font-size: 30px; color: var(--ink); }
  .letterhead .contact {
    position: absolute; right: 34px; top: 100px;
    border-left: 1px solid var(--red);
    padding-left: 12px;
    font-size: 9px; line-height: 16px; color: var(--muted);
  }
  .contact-row { display: flex; align-items: center; gap: 6px; }
  .letterhead .footer-address {
    position: absolute; left: 40px; bottom: 24px;
    font-size: 11px; font-weight: 700; letter-spacing: 1px;
  }
  .red-edge { position: absolute; left: 0; right: 0; bottom: 0; height: 8px; background: var(--red); }

  /* Business cards */
  .card {
    position: absolute; width: 300px; height: 172px;
    background: var(--card);
    box-shadow: 0 2px 8px rgba(0,0,0,.2);
    overflow: hidden;
  }
  .card .red-edge { height: 5px; }
  .card-front { left: 560px; top: 120px; }
  .card-front .wordmark {
    position: absolute; left: 0; right: 0; top: 64px;
    text-align: center; font-size: 40px; color: var(--card-mark);
  }
  .card-back { left: 880px; top: 120px; display: flex; align-items: center; }
  .card-back .wordmark { width: 140px; text-align: center; font-size: 20px; color: var(--card-mark); }
  .card-back .divider { width: 1px; height: 80px; background: #555; }
  .card-back .details { padding-left: 14px; font-size: 8px; line-height: 14px; color: var(--card-text); }
  .card-back .person-name { color: var(--red); font-size: 11px; font-weight: 700; letter-spacing: 1.5px; }
  .card-back .person-role { margin-bottom: 6px; }

  /* Envelope */
  .envelope {
    position: absolute; left: 560px; top: 340px;
    width: 620px; height: 310px;
    background: var(--paper);
    box-shadow: 0 2px 8px rgba(0,0,0,.12);
  }
  .envelope .wordmark { position: absolute; left: 36px; top: 34px; font-size: 30px; }
  .envelope .window {
    position: absolute; left: 36px; top: 100px;
    width: 280px; height: 110px;
    background: var(--red); border-radius: 14px;
  }
  .envelope .footer-address {
    position: absolute; left: 36px; bottom: 22px;
    font-size: 11px; font-weight: 700; letter-spacing: 1px;
  }
</style>
</head>
<body>

<svg width="0" height="0" style="position:absolute">
  <defs>
    <symbol id="i-phone" viewBox="0 0 10 10"><path d="M2 1l2 2-1 1c.6 1.3 1.7 2.4 3 3l1-1 2 2-1.5 1.5C4.5 9 1 5.5.5 2.5z" fill="#c02424"/></symbol>
    <symbol id="i-mail" viewBox="0 0 10 10"><rect x=".5" y="2" width="9" height="6" fill="none" stroke="#c02424"/><path d="M.5 2l4.5 3.5L9.5 2" fill="none" stroke="#c02424"/></symbol>
    <symbol id="i-web" viewBox="0 0 10 10"><circle cx="5" cy="5" r="4.3" fill="none" stroke="#c02424"/><path d="M.7 5h8.6M5 .7c-2.5 2.6-2.5 6 0 8.6M5 .7c2.5 2.6 2.5 6 0 8.6" fill="none" stroke="#c02424" stroke-width=".8"/></symbol>
  </defs>
</svg>

<section class="letterhead">
  <div class="wordmark">Meridale</div>
  <div class="contact">
    <div class="contact-row"><svg class="icon"><use href="#i-phone"/></svg>0145-220-318</div>
    <div class="contact-row"><svg class="icon"><use href="#i-mail"/></svg>office@meridale-mail.com</div>
    <div class="contact-row"><svg class="icon"><use href="#i-web"/></svg>www.meridale.com</div>
  </div>
  <div class="footer-address">#12, Meridale House, Grove Street, Your Country - 204871</div>
  <div class="red-edge"></div>
</section>

<section class="card card-front">
  <div class="wordmark">Meridale</div>
  <div class="red-edge"></div>
</section>

<section class="card card-back">
  <div class="wordmark">Meridale</div>
  <div class="divider"></div>
  <div class="details">
    <div class="person-name">ADA LORNE</div>
    <div class="person-role">Founder/CEO</div>
    <div class="contact-row"><svg class="icon"><use href="#i-phone"/></svg>0145-220-318</div>
    <div class="contact-row"><svg class="icon"><use href="#i-mail"/></svg>office@meridale-mail.com</div>
    <div class="contact-row"><svg class="icon"><use href="#i-web"/></svg>www.meridale.com</div>
  </div>
  <div class="red-edge"></div>
</section>

<section class="envelope">
  <div class="wordmark">Meridale</div>
  <div class="window"></div>
  <div class="footer-address">#12, Meridale House, Grove Street, Your Country - 204871</div>
  <div class="red-edge"></div>
</section>

</body>
</html>
```